Assorted Banner Ads

Create standard sized banner ads (300x250, 728x90, 160x600) using logo and create exciting ads using collateral provided and your own ideas.

```html
<!DOCTYPE html>
<html lang="en">
<head>
<meta charset="utf-8">
<title>Harbor Lock Escape – Banner Set</title>
<link href="https://fonts.googleapis.com/css2?family=Oswald:wght@300;400&family=Montserrat:wght@600&family=Open+Sans:wght@400&display=swap" rel="stylesheet">
<style>
  :root {
    --board: #2f2b29;
    --brand-green: #2f8540;
    --paper: #ffffff;
    --ink: #161616;
    --label: #e6e2de;
    --wood-dark: #5a2a0c;
    --wood-mid: #a4561c;
    --wood-light: #e0a35c;
  }
  html, body { margin: 0; padding: 0; }
  body {
    width: 1200px; height: 1200px; overflow: hidden;
    background: var(--board); position: relative;
    font-family: "Open Sans", sans-serif;
  }
  .edge-bar { position: absolute; left: 0; width: 1200px; background: var(--brand-green); }
  .edge-bar--top { top: 0; height: 10px; }
  .edge-bar--bottom { bottom: 0; height: 14px; }
  .size-label {
    position: absolute; margin: 0; color: var(--label);
    font-size: 13px; line-height: 1;
  }
  .banner { position: absolute; display: block; box-shadow: 0 2px 6px rgba(0,0,0,.45); }
  .banner--leaderboard { left: 309px; top: 296px; width: 582px; height: 72px; }
  .banner--rectangle { left: 309px; top: 424px; width: 240px; height: 200px; }
  .banner--skyscraper { left: 600px; top: 424px; width: 128px; height: 480px; }
  .headline { font-family: "Oswald", sans-serif; font-weight: 300; fill: var(--brand-green); }
  .subline { font-family: "Oswald", sans-serif; font-weight: 300; fill: var(--ink); }
  .cta-text { font-family: "Oswald", sans-serif; font-weight: 400; fill: var(--paper); }
  .brand-name { font-family: "Montserrat", sans-serif; font-weight: 600; fill: var(--paper); letter-spacing: 1px; }
  .brand-name--compact { letter-spacing: .4px; }
  .brand-mark { fill: var(--paper); }
  .green-field { fill: var(--brand-green); }
  .white-panel { fill: var(--paper); }
  .cta-badge { fill: var(--brand-green); stroke: var(--paper); stroke-width: 4; }
  .curve-rule { fill: none; stroke: var(--paper); stroke-width: 3; }
</style>
</head>
<body>
  <div class="edge-bar edge-bar--top"></div>

  <p class="size-label" style="left:310px;top:266px;">728-90</p>
  <svg class="banner banner--leaderboard" viewBox="0 0 728 90" aria-label="728 by 90 banner">
    <defs>
      <linearGradient id="woodA" x1="0" y1="0" x2="1" y2="1">
        <stop offset="0" stop-color="var(--wood-light)"/>
        <stop offset=".5" stop-color="var(--wood-mid)"/>
        <stop offset="1" stop-color="var(--wood-dark)"/>
      </linearGradient>
    </defs>
    <g role="img" aria-label="Photo of a ship cabin escape room interior">
      <rect x="120" y="0" width="300" height="90" fill="url(#woodA)"/>
      <rect x="660" y="0" width="68" height="90" fill="url(#woodA)"/>
    </g>
    <rect class="white-panel" x="418" y="0" width="243" height="90"/>
    <path class="green-field" d="M0 0 H170 Q150 55 125 90 H0 Z"/>
    <path class="curve-rule" d="M170 0 Q150 55 125 90"/>
    <circle class="brand-mark" cx="66" cy="22" r="9"/>
    <text class="brand-name" x="66" y="55" font-size="13" text-anchor="middle">HARBOR LOCK</text>
    <text class="brand-name" x="66" y="68" font-size="8" text-anchor="middle">ESCAPE ROOM</text>
    <text class="headline" x="430" y="39" font-size="18">Can you Escape in 60 Minutes?</text>
    <text class="subline" x="431" y="63" font-size="18">Find Clues! Slove Puzzels!</text>
    <circle class="cta-badge" cx="664" cy="48" r="33"/>
    <text class="cta-text" x="663" y="46" font-size="15" text-anchor="middle">READ</text>
    <text class="cta-text" x="664" y="64" font-size="15" text-anchor="middle">MORE</text>
  </svg>

  <p class="size-label" style="left:310px;top:399px;">300-250</p>
  <svg class="banner banner--rectangle" viewBox="0 0 300 250" aria-label="300 by 250 banner">
    <defs>
      <linearGradient id="woodB" x1="0" y1="0" x2="0" y2="1">
        <stop offset="0" stop-color="var(--wood-mid)"/>
        <stop offset=".45" stop-color="var(--wood-light)"/>
        <stop offset="1" stop-color="var(--wood-dark)"/>
      </linearGradient>
    </defs>
    <rect role="img" aria-label="Photo of a ship cabin escape room with windows and lantern" x="0" y="0" width="300" height="195" fill="url(#woodB)"/>
    <rect class="white-panel" x="0" y="195" width="300" height="55"/>
    <path class="green-field" d="M0 0 H141 Q90 80 0 105 Z"/>
    <path class="curve-rule" d="M141 0 Q90 80 0 105"/>
    <circle class="brand-mark" cx="48" cy="20" r="8"/>
    <text class="brand-name brand-name--compact" x="48" y="45" font-size="10" text-anchor="middle">HARBOR LOCK</text>
    <text class="brand-name brand-name--compact" x="48" y="55" font-size="6" text-anchor="middle">ESCAPE ROOM</text>
    <text class="headline" x="7" y="219" font-size="18">Can you Escape in 60 Minutes?</text>
    <text class="subline" x="8" y="241" font-size="18">Find Clues! Slove Puzzels!</text>
    <circle class="cta-badge" cx="257" cy="210" r="34"/>
    <text class="cta-text" x="256" y="205" font-size="18" text-anchor="middle">READ</text>
    <text class="cta-text" x="257" y="224" font-size="18" text-anchor="middle">MORE</text>
  </svg>

  <p class="size-label" style="left:598px;top:399px;">160-600</p>
  <svg class="banner banner--skyscraper" viewBox="0 0 160 600" aria-label="160 by 600 banner">
    <defs>
      <linearGradient id="woodC" x1="0" y1="0" x2="1" y2="1">
        <stop offset="0" stop-color="var(--wood-mid)"/>
        <stop offset=".5" stop-color="var(--wood-light)"/>
        <stop offset="1" stop-color="var(--wood-dark)"/>
      </linearGradient>
    </defs>
    <g role="img" aria-label="Photo of a ship cabin escape room with lantern and desk">
      <rect x="0" y="0" width="160" height="403" fill="url(#woodC)"/>
      <rect x="0" y="550" width="160" height="50" fill="var(--wood-dark)"/>
    </g>
    <rect class="white-panel" x="0" y="403" width="160" height="147"/>
    <path class="green-field" d="M0 0 H160 V85 Q90 108 0 125 Z"/>
    <path class="curve-rule" d="M160 85 Q90 108 0 125"/>
    <circle class="brand-mark" cx="78" cy="28" r="12"/>
    <text class="brand-name" x="78" y="68" font-size="15" text-anchor="middle">HARBOR LOCK</text>
    <text class="brand-name" x="78" y="81" font-size="9" text-anchor="middle">ESCAPE ROOM</text>
    <text class="headline" x="80" y="437" font-size="26" text-anchor="middle">Can you Escape</text>
    <text class="headline" x="78" y="467" font-size="26" text-anchor="middle">in 60 Minutes?</text>
    <text class="subline" x="80" y="491" font-size="15" text-anchor="middle">Find Clues! Slove Puzzels!</text>
    <circle class="cta-badge" cx="83" cy="536" r="34"/>
    <text class="cta-text" x="83" y="533" font-size="18" text-anchor="middle">READ</text>
    <text class="cta-text" x="83" y="552" font-size="18" text-anchor="middle">MORE</text>
  </svg>

  <div class="edge-bar edge-bar--bottom"></div>
</body>
</html>
```